Webdesign für Maklerbüro
Zielgruppe
Wir sind ein Maklerbüro aus Nürnberg, das sich auf den Verkauf von Eigentumswohnungen und Häuser spezialisiert hat. Mit der neuen Seite möchten wir vor allem Eigentümer ansprechen und über unsere Arbeitsweise informieren. Der Hauptzweck ist damit die Akquise von neuen Objekten, für die Vermittlung. Die Zielgruppe sind vornehmlich Immobilienbesitzer im Alter 40+ und im gehobenen Preissegment.
Aufgabenstellung
Beim Design bitte an den Vorgaben des Logo (Datei beigefügt) orientieren. Bilder und Texte können durch 'Platzhalter' ersetzt werden.
Grundsätzlich stellt es für uns kein Problem dar, sich an Template-Vorlagen zu orientieren. Wir stellen uns eine Seite mit Pfiff und Ideenreichtum – einfach weg vom Standard – vor. Wir verkaufen Immobilien, aber vom verstaubten Krawattenträger sind wir weit entfernt. Wir sind ein junges Unternehmen, das neue Marketingwege beschreitet. Unsere Webseite muss das ausdrücken. Kein Standard, und damit auch keine Standard-Webseite. Designs, die uns gut gefallen (und in die Richtung es auch gehen kann) haben wir beigefügt.

```html
<!DOCTYPE html>
<html lang="de">
<head>
<meta charset="utf-8">
<title>Frankenhaus – Immobilienmakler Nürnberg</title>
<link rel="stylesheet" href="https://fonts.googleapis.com/css2?family=Open+Sans:wght@600;700&family=Source+Sans+3:ital,wght@0,400;0,600;1,400&display=swap">
<style>
:root{
  --navy:#171f3a;
  --navy-soft:#222b4a;
  --accent:#4f73c8;
  --strip:#1e88d8;
  --page:#f2f2f2;
  --grey:#bcbdc4;
  --text:#1d2540;
  --white:#ffffff;
}
*{box-sizing:border-box;margin:0;padding:0}
html,body{width:1200px;height:2855px;overflow:hidden}
body{background:var(--page);font-family:"Source Sans 3",Arial,sans-serif;color:var(--text);position:relative}
.abs{position:absolute}
.btn-frame{position:absolute;border:3px solid var(--accent);display:flex;align-items:center;justify-content:center;font-size:25px}
.section-title{position:absolute;left:0;width:1200px;text-align:center;font-size:31px;font-weight:400;color:var(--text)}

/* hero */
.hero{position:absolute;left:0;top:0;width:1200px;height:590px;
  background:linear-gradient(180deg,#4c5a78 0%,#6f7590 35%,#8b8a98 60%,#6b6470 80%,#4a4550 100%);
  clip-path:polygon(0 0,1200px 0,1200px 548px,598px 588px,0 540px)}
.nav-bar{position:absolute;left:0;top:80px;width:1099px;height:43px;background:rgba(23,31,58,.92)}
.brand{position:absolute;left:113px;top:104px;font-family:"Open Sans",Arial,sans-serif;font-weight:600;font-size:28px;color:var(--white);letter-spacing:1px}
.brand-mark{display:inline-block;width:14px;height:14px;background:var(--white);margin-right:10px;vertical-align:1px}
.menu{position:absolute;left:1057px;top:87px;width:35px}
.menu span{display:block;height:4px;background:var(--white);margin-bottom:7px}
.hero-claim{position:absolute;left:0;top:288px;width:1200px;text-align:center;font-family:"Open Sans",Arial,sans-serif;font-weight:600;font-size:27px;color:var(--white)}
.hero-btn{left:459px;top:430px;width:277px;height:49px;color:var(--white);font-family:"Open Sans",Arial,sans-serif;font-weight:700;font-size:23px}

/* benefits */
.benefit{position:absolute;top:712px;width:330px;height:95px}
.benefit svg{position:absolute;left:0;top:0}
.benefit p{position:absolute;left:100px;top:2px;width:207px;font-size:10.5px;line-height:14px;text-align:justify;color:var(--navy)}

/* valuation band */
.valuation{position:absolute;left:0;top:875px;width:1200px;height:222px;
  background:linear-gradient(90deg,#0d0f14 0%,#2a2c33 30%,#6d6f77 45%,#3a3c44 60%,#9a9ca4 70%,#1a1c22 85%,#0d0f14 100%);
  clip-path:polygon(0 0,598px 50px,1200px 0,1200px 172px,598px 222px,0 172px)}
.valuation h2{position:absolute;left:111px;top:89px;font-family:"Open Sans",Arial,sans-serif;font-weight:700;font-size:24px;color:var(--white)}
.valuation p{position:absolute;left:214px;top:124px;font-size:16px;color:var(--white)}
.valuation-btn{left:882px;top:965px;width:223px;height:49px;color:var(--white)}

/* process carousel */
.step-icon-box{position:absolute;left:205px;top:1198px;width:193px;height:261px;background:var(--navy)}
.step-tab{position:absolute;left:496px;top:1198px;width:193px;height:261px;background:var(--grey)}
.step-card{position:absolute;top:1217px;height:221px;color:var(--white)}
.step-card h3{position:absolute;top:32px;font-size:25px;font-weight:400}
.step-card p{position:absolute;left:38px;top:84px;font-size:21px;line-height:24px}
.step-active{left:398px;width:308px;background:var(--navy)}
.step-active h3{left:65px}
.step-next{left:706px;width:291px;background:var(--grey)}
.step-next h3{left:48px;color:#eef0f5}
.step-next p{left:22px;color:#eef0f5}
.arrow{position:absolute;top:1312px;width:37px;height:37px;border-radius:50%;background:var(--navy);color:var(--white);font-size:20px;display:flex;align-items:center;justify-content:center}
.cta-btn{left:463px;top:1499px;width:268px;height:49px;color:var(--navy)}

/* testimonials */
.testimonials{position:absolute;left:0;top:1557px;width:1200px;height:400px;background:var(--navy);
  clip-path:polygon(0 0,598px 48px,1200px 0,1200px 400px,0 400px)}
.testimonials h2{position:absolute;left:0;top:101px;width:1200px;text-align:center;font-size:31px;font-weight:400;color:var(--white)}
.quote-mark{position:absolute;left:50px;top:148px;font-family:"Open Sans",Arial,sans-serif;font-weight:700;font-size:190px;line-height:1;color:#8d8f96}
.quote-text{position:absolute;left:197px;top:184px;width:750px;font-size:15.5px;line-height:26.5px;color:var(--white)}
.quote-author{position:absolute;left:797px;top:265px;width:150px;text-align:right;font-style:italic;font-size:14.5px;color:#8d8f96}
.portrait{position:absolute;left:1030px;top:83px;width:175px;height:198px;transform:rotate(-4deg);
  background:radial-gradient(circle at 50% 45%,#9a9a9a 0%,#555 45%,#1c1c1c 100%)}
.dots{position:absolute;left:566px;top:1891px}
.dots span{display:inline-block;width:17px;height:17px;border-radius:50%;background:#c9cacf;margin-right:5px}
.dots span.on{background:var(--accent)}

/* map */
.map{position:absolute;left:0;top:1911px;width:1200px;height:295px;
  background:linear-gradient(110deg,#e9e4da 0%,#d7e4d0 22%,#a8cbeb 40%,#e8e4dc 58%,#d9e6cf 75%,#a8cbeb 88%,#e7e3da 100%);
  clip-path:polygon(0 0,598px 48px,1200px 0,1200px 272px,598px 294px,0 244px)}

/* contact */
.contact-row{position:absolute;left:110px;height:50px;width:300px}
.contact-row svg{position:absolute;left:0;top:0}
.contact-row span{position:absolute;left:85px;top:0;font-size:16px;line-height:27px;color:var(--navy)}
.field{position:absolute;height:35px;background:var(--navy);border-right:6px solid var(--strip);color:var(--white);font-size:14.5px;padding:9px 16px}
.message{left:528px;top:2465px;width:577px;height:194px}
.send-btn{left:528px;top:2683px;width:577px;height:49px;color:var(--navy);font-size:25px}

/* footer */
.footer{position:absolute;left:0;top:2809px;width:1200px;height:46px;background:var(--navy);color:var(--white);font-size:17px}
.footer a{position:absolute;top:13px;color:var(--white);text-decoration:none}
</style>
</head>
<body>

<header>
  <div class="hero" role="img" aria-label="Foto eines modernen Einfamilienhauses in der Abenddämmerung"></div>
  <div class="nav-bar"></div>
  <div class="brand"><span class="brand-mark"></span>FRANKENHAUS</div>
  <div class="menu"><span></span><span></span><span></span></div>
  <h1 class="hero-claim">Ihr Immobilienmakler für die Metropolregion Nürnberg.</h1>
  <div class="btn-frame hero-btn">Wer wir sind.</div>
</header>

<section>
  <h2 class="section-title" style="top:617px">Die richtige Wahl des Immobilienmaklers.</h2>

  <div class="benefit" style="left:66px">
    <svg width="82" height="90" viewBox="0 0 82 90" fill="none" stroke="#171f3a" stroke-width="3" stroke-linejoin="round">
      <circle cx="41" cy="32" r="26"/><circle cx="41" cy="32" r="16"/>
      <path d="M33 36v-7l8-6 8 6v7z"/>
      <path d="M22 50 6 80l14-3 6 12 12-26"/><path d="M60 50l16 30-14-3-6 12-12-26"/>
    </svg>
    <p>Wir kennen den regionalen Markt genau und begleiten Sie mit Erfahrung, Transparenz und persönlicher Betreuung vom ersten Gespräch bis zum sicheren Abschluss beim Notar. Ihr Vorteil.</p>
  </div>

  <div class="benefit" style="left:443px">
    <svg width="82" height="90" viewBox="0 0 82 90" fill="none" stroke="#171f3a" stroke-width="3" stroke-linejoin="round">
      <path d="M30 86V72c-14-2-20-10-18-20L6 46l8-8c2-20 18-32 38-30 20 2 30 20 26 40-2 10-8 16-14 20v18"/>
      <circle cx="38" cy="38" r="8"/><circle cx="58" cy="30" r="7"/><circle cx="56" cy="52" r="6"/>
    </svg>
    <p>Mit durchdachten Strategien, moderner Präsentation und klarer Kommunikation erzielen wir für Ihre Immobilie den bestmöglichen Preis – schnell, diskret und verlässlich für Sie.</p>
  </div>

  <div class="benefit" style="left:820px">
    <svg width="82" height="90" viewBox="0 0 82 90" fill="none" stroke="#171f3a" stroke-width="3.5" stroke-linejoin="round">
      <path d="M4 46 41 8l38 38"/><path d="M14 36v50h14V62h16"/>
      <path d="M60 86 46 72c-6-6 0-16 8-12l6 4 6-4c8-4 14 6 8 12z"/>
    </svg>
    <p>Wir hören zu, verstehen Ihre Wünsche und finden gemeinsam mit Ihnen die passende Lösung. Vertrauen, Ehrlichkeit und Engagement stehen bei jedem Auftrag im Mittelpunkt.</p>
  </div>
</section>

<section class="valuation" role="img" aria-label="Foto eines Handschlags zwischen Geschäftsleuten">
  <h2>Professionelle Immobilienbewertung</h2>
  <p>Was ist meine Immobilie Wert? Wir finden den richtigen Preis für Sie.</p>
</section>
<div class="btn-frame valuation-btn">Jetzt Anfragen!</div>

<section>
  <h2 class="section-title" style="top:1122px">Rundum Sorglos Vertrieb Ihrer Immobilie.</h2>
  <div class="step-tab"></div>
  <div class="step-icon-box">
    <svg class="abs" style="left:38px;top:62px" width="118" height="126" viewBox="0 0 118 126" fill="none" stroke="#fff" stroke-width="3.5" stroke-linejoin="round">
      <path d="M4 62 59 6l55 56"/><path d="M18 12h14v20"/><path d="M18 50v66h82V50"/>
      <path d="M40 66h38l-19-20z"/><path d="M32 80h14v20H32zM50 90h16v26H50zM72 80h14v20H72z"/>
      <path d="M2 120h114"/>
    </svg>
  </div>
  <div class="step-card step-active">
    <h3>Objektaufnahme</h3>
    <p>Detallierte Einwertung, Preisfindung, Vermessung und Fotografie Ihrer Immobilie.</p>
  </div>
  <div class="step-card step-next">
    <h3>Vermarktung</h3>
    <p>Gemeinsame Festlegung eines Vermarktungs- &amp; Präsentationskonzeptes für Ihre Immobilie.</p>
  </div>
  <div class="arrow" style="left:75px">&lt;</div>
  <div class="arrow" style="left:1087px">&gt;</div>
  <div class="btn-frame cta-btn">Termin vereinbaren</div>
</section>

<section class="testimonials">
  <h2>Das sagen Unsere Kunden.</h2>
  <div class="quote-mark">”</div>
  <p class="quote-text">Ich würde Herrn Brennholt als freundlich, zuverlässig und integer beschreiben. Eigenschaften, die in dieser Kombination nicht branchentypisch sind. Er hat uns beim Erwerb einer Eigentumswohnung sehr kompetent beraten und bis zum Abschluss herausragend begleitet. Ich kann die "Lukas Brennholt Immobilienberatung" wirklich uneingeschränkt empfehlen.</p>
  <div class="quote-author">Peter M. (Käufer)</div>
  <div class="portrait" role="img" aria-label="Schwarzweiß-Porträtfoto eines Kunden"></div>
</section>
<div class="dots"><span class="on"></span><span></span><span></span></div>

<div class="map" role="img" aria-label="Stadtplan mit Lage des Maklerbüros"></div>

<section>
  <h2 class="section-title" style="top:2258px">Treten Sie mit Uns in Kontakt.</h2>

  <div class="contact-row" style="top:2352px">
    <svg width="44" height="48" viewBox="0 0 44 48" fill="none" stroke="#171f3a" stroke-width="2">
      <path d="M6 46V4h20v42M26 16h12v30M2 46h40"/>
      <path d="M10 9h4v4h-4zM18 9h4v4h-4zM10 18h4v4h-4zM18 18h4v4h-4zM10 27h4v4h-4zM18 27h4v4h-4zM30 22h4v4h-4zM30 31h4v4h-4zM14 38h4v8h-4z"/>
    </svg>
    <span>Lindenhofweg 7<br>90402 Nürnberg</span>
  </div>
  <div class="contact-row" style="top:2445px">
    <svg width="48" height="48" viewBox="0 0 48 48" fill="none" stroke="#171f3a" stroke-width="2" stroke-linejoin="round">
      <path d="M10 4 4 10c0 18 16 34 34 34l6-6-9-9-6 5C22 31 17 26 14 19l5-6z"/>
    </svg>
    <span style="top:10px">+49 911 5550 12 40</span>
  </div>
  <div class="contact-row" style="top:2533px">
    <svg width="44" height="48" viewBox="0 0 44 48" fill="none" stroke="#171f3a" stroke-width="2">
      <rect x="10" y="2" width="26" height="44" rx="4"/><path d="M10 9h26M10 38h26M20 42h6"/>
    </svg>
    <span style="top:10px">+49 176 5550 27 88</span>
  </div>
  <div class="contact-row" style="top:2624px">
    <svg width="48" height="32" viewBox="0 0 48 32" fill="none" stroke="#171f3a" stroke-width="2">
      <rect x="2" y="3" width="44" height="27"/><path d="M2 3l22 18L46 3M2 30l16-14M46 30 30 16"/>
    </svg>
    <span style="top:0">kontakt@frankenhaus-makler.de</span>
  </div>

  <form>
    <div class="field" style="left:528px;top:2354px;width:269px">Ihr Name*</div>
    <div class="field" style="left:836px;top:2354px;width:269px">Straße, Hausnummer*</div>
    <div class="field" style="left:528px;top:2408px;width:269px">E-Mail*</div>
    <div class="field" style="left:836px;top:2408px;width:269px">Postleitzahl, Ort*</div>
    <div class="field message">Ihre Nachricht an Uns.</div>
    <div class="btn-frame send-btn">Senden</div>
  </form>
</section>

<footer class="footer">
  <a href="#" style="left:483px">Impressum</a>
  <a href="#" style="left:620px">Datenschutz</a>
</footer>

</body>
</html>
```